VORMTEK
Guardline Unified Networks
Creative Brief
Professional
Nadim Bu Haydar
Executive Director - Partner
P. O. Box 71862 Jeddah 23847 Saudi Arabia
nbuhaydar@vormtek-example.com
www.vormtek-example.com
Full Company Name: The full name of the company is Guardline Unified Networks. Company Description: The company is a security and surveillance solutions retailer and integrator that is focused on bringing high tech, high impact, and high value security solutions Mission Statement: Guardline Unified Networks brings to the regional security arena the necessary solutions that capitalize on the advances in technology, and give the clients more control, functionality, and security. The employees of Guardline Unified Networks are its ambassadors to the clients, and the company is committed to their success, growth, and development, as much as it is committed to the success, growth, and profitability of its stakeholders. Vision: Guardline Unified Networks (GUN) aims to become the leading regional provider of high-tech, high impact, high value security solutions. Values: Professional delivery, and superior service. Long-term relationships Continued innovation, and development. Excellent communication, and ability to understand, and forecast the needs of clients Transparency and Fairness towards clients, employees, and stakeholders. Competitive Advantage: Our competitive advantage lay in our commitment to bringing to the local market the high tech, high impact, high value security solutions. The first agency that we secured (Qelto - www.qelto-example.com) is the only company that combined digital surveillance with analytics and biometrics, along with indexing video footage. It is such companies, along with our professional standard in delivery and installation that will set us apart form the local and regional competitors. Target Market: Our target market is segmented into the following groups: - Financial Services - Government (Ministries, airports, sea ports, traffic, etc.) - Healthcare - Distributors (secondary distributors of our products) - Educational - Large residential communities (compounds), and VIP - Commercial and residential The first three are our immediate top priority. The distributors also will be a key target for us to expand our reach through their established network. The last three are segments that we envision growth in at later stages. Our target local will be Saudi Arabia initially. We hold the agencies for the GCC market, and thus plan on expanding into those markets by the second or third year of operation.
Will mirror the front of the card, but will have the Arabic information.

```html
<!DOCTYPE html>
<html lang="en">
<head>
<meta charset="utf-8">
<title>VORMTEK Stationery</title>
<link href="https://fonts.googleapis.com/css2?family=Montserrat:wght@700&family=Open+Sans:wght@400;600&family=Tajawal:wght@400;700&display=swap" rel="stylesheet">
<style>
  :root{
    --bg:#e6e3de;
    --paper:#ffffff;
    --green-dark:#1f7a2e;
    --green:#3c9a35;
    --green-light:#8cc63f;
    --ink:#4a4a4a;
    --ink-soft:#7b7b7b;
  }
  *{margin:0;padding:0;box-sizing:border-box}
  html,body{width:1200px;height:715px;overflow:hidden;background:var(--bg)}
  body{position:relative;font-family:"Open Sans",Arial,sans-serif;color:var(--ink)}

  .wordmark{display:flex;align-items:center;gap:6px;font-family:"Montserrat",Arial,sans-serif;font-weight:700;color:var(--green-dark);letter-spacing:.02em;line-height:1}
  .wordmark .dot{border-radius:50%;background:var(--green)}
  .tagline{font-size:6px;letter-spacing:.12em;text-transform:uppercase;color:var(--ink-soft)}

  /* Letterhead */
  .letterhead{position:absolute;left:36px;top:34px;width:564px;height:650px;background:var(--paper);box-shadow:0 2px 6px rgba(0,0,0,.18)}
  .letterhead .brand{position:absolute;top:48px;left:0;right:0;display:flex;flex-direction:column;align-items:center;gap:6px}
  .letterhead .wordmark{font-size:30px}
  .letterhead .wordmark .dot{width:22px;height:22px}
  .letterhead .tagline{font-size:7px}
  .letterhead .footer{position:absolute;bottom:30px;left:0;right:0;text-align:center;font-size:7px;color:var(--ink-soft);line-height:2}
  .letterhead .footer .web{letter-spacing:.35em}
  .letterhead .band{position:absolute;left:0;right:0;bottom:0;height:8px;background:linear-gradient(90deg,var(--green-dark),var(--green-light))}

  /* Business cards */
  .card{position:absolute;top:163px;width:204px;height:120px;overflow:hidden;background:linear-gradient(135deg,var(--green-dark),var(--green-light));box-shadow:0 2px 5px rgba(0,0,0,.2)}
  .card-front{left:648px}
  .card-back{left:864px}
  .card .sheet{position:absolute;top:-40px;width:250px;height:200px;border-radius:50%;background:var(--paper)}
  .card-front .sheet{left:-72px}
  .card-back .sheet{right:-72px}
  .card .wordmark{position:absolute;top:52px;font-size:11px}
  .card .wordmark .dot{width:9px;height:9px}
  .card-front .wordmark{left:100px}
  .card-back .wordmark{left:14px}
  .card .details{position:absolute;top:12px;font-size:4.6px;line-height:1.55;color:var(--ink)}
  .card-front .details{left:10px;width:86px}
  .card-back .details{right:10px;width:86px;text-align:right;direction:rtl;font-family:"Tajawal","Open Sans",sans-serif;font-size:5px}
  .card .name{font-size:7px;font-weight:600;color:var(--green-dark)}
  .card-back .name{font-size:9px;font-weight:700}
  .card .role{margin-bottom:8px;color:var(--ink-soft)}
  .card .gap{margin-top:6px}

  /* Envelope */
  .envelope{position:absolute;left:612px;top:432px;width:560px;height:250px;background:var(--paper);box-shadow:0 2px 6px rgba(0,0,0,.18)}
  .envelope .flap{position:absolute;left:0;top:0;width:560px;height:110px}
  .envelope .flap-web{position:absolute;top:30px;left:0;right:0;text-align:center;font-size:6.5px;letter-spacing:.4em;color:#e9f5dc}
  .envelope .brand{position:absolute;left:34px;top:140px;display:flex;flex-direction:column;gap:4px}
  .envelope .wordmark{font-size:20px}
  .envelope .wordmark .dot{width:15px;height:15px}
  .envelope .footer{position:absolute;bottom:14px;left:0;right:0;text-align:center;font-size:6px;color:var(--ink-soft)}
  .envelope .band{position:absolute;left:0;right:0;bottom:0;height:4px;background:linear-gradient(90deg,var(--green-dark),var(--green-light))}
</style>
</head>
<body>

<section class="letterhead">
  <div class="brand">
    <div class="wordmark"><span class="dot"></span>VORMTEK</div>
    <div class="tagline">Guardline Unified Networks</div>
  </div>
  <div class="footer">
    <div>P. O. Box 71862 | Jeddah 23847 | Saudi Arabia | P: +966 (2) 555-0142 | F: +966 (2) 555-0178</div>
    <div class="web">www.vormtek-example.com</div>
  </div>
  <div class="band"></div>
</section>

<section class="card card-front">
  <div class="sheet"></div>
  <div class="details">
    <div class="name">Nadim Bu Haydar</div>
    <div class="role">Executive Director - Partner</div>
    <div>P. O. Box 71862</div>
    <div>Jeddah 23847, Saudi Arabia</div>
    <div class="gap">T: +966 (2) 555-0142</div>
    <div>F: +966 (2) 555-0178</div>
    <div>M: +966 (5) 0000-4219</div>
    <div class="gap">nbuhaydar@vormtek-example.com</div>
    <div>www.vormtek-example.com</div>
  </div>
  <div class="wordmark"><span class="dot"></span>VORMTEK</div>
</section>

<section class="card card-back">
  <div class="sheet"></div>
  <div class="wordmark"><span class="dot"></span>VORMTEK</div>
  <div class="details" lang="ar">
    <div class="name">نديم بو حيدر</div>
    <div class="role">المدير التنفيذي - شريك</div>
    <div>ص.ب ٧١٨٦٢</div>
    <div>جدة ٢٣٨٤٧، المملكة العربية السعودية</div>
    <div class="gap">هاتف: ٥٥٥٠١٤٢ (٢) ٩٦٦+</div>
    <div>فاكس: ٥٥٥٠١٧٨ (٢) ٩٦٦+</div>
    <div>جوال: ٠٠٠٠٤٢١٩ (٥) ٩٦٦+</div>
  </div>
</section>

<section class="envelope">
  <svg class="flap" viewBox="0 0 560 110" preserveAspectRatio="none" aria-hidden="true">
    <defs>
      <linearGradient id="flapGreen" x1="0" y1="0" x2="0" y2="1">
        <stop offset="0" stop-color="#1f7a2e"/>
        <stop offset="1" stop-color="#5fae3a"/>
      </linearGradient>
    </defs>
    <path d="M0 0H560V62Q280 150 0 62Z" fill="url(#flapGreen)"/>
  </svg>
  <div class="flap-web">www.vormtek-example.com</div>
  <div class="brand">
    <div class="wordmark"><span class="dot"></span>VORMTEK</div>
    <div class="tagline">Guardline Unified Networks</div>
  </div>
  <div class="footer">P. O. Box 71862 | Jeddah 23847 | Saudi Arabia</div>
  <div class="band"></div>
</section>

</body>
</html>
```